PDF-Dokumente für Vermietung und Verwaltung von Immobilien
Zielgruppe
WohnKranich, Vermietung und Verwaltung von Immoblien
Aufgabenstellung
Wir haben ganz viele Dokumente, die als PDF erstellt werden sollen, Einheitlich im CI Design, mit Logo etc. Manche PDFS müssen ausfüllbar sein andere sind einfach nur zum Drucken. es sind ca 10-20 Word/PDF Dokumente.

```html
<!DOCTYPE html>
<html lang="de">
<head>
<meta charset="utf-8">
<title>Bürgschaftsurkunde – WohnKranich</title>
<link rel="stylesheet" href="https://fonts.googleapis.com/css2?family=Open+Sans:wght@400;600;700&family=Tinos&display=swap">
<style>
  :root {
    --navy: #323c52;
    --ink: #2c3550;
    --rule: #5a6175;
    --grey: #8a8f99;
    --paper: #ffffff;
  }
  * { margin: 0; padding: 0; box-sizing: border-box; }
  html, body { width: 849px; height: 1200px; overflow: hidden; background: var(--paper); }
  .sheet {
    position: relative; width: 849px; height: 1200px; overflow: hidden;
    font-family: "Open Sans", sans-serif; color: var(--ink);
  }
  .abs { position: absolute; }

  .brand { right: 40px; top: 96px; display: flex; align-items: center; gap: 10px; }
  .brand-mark { width: 16px; height: 16px; background: var(--navy); }
  .brand-name { font-family: "Open Sans", sans-serif; font-weight: 600; font-size: 20px; color: var(--navy); white-space: nowrap; }
  .brand-tag { right: 40px; top: 126px; font-size: 8px; letter-spacing: 0.5px; color: var(--grey); white-space: nowrap; }

  .title-box { left: 71px; top: 149px; width: 311px; height: 44px; background: var(--navy); color: #fff;
    font-weight: 700; font-size: 20px; letter-spacing: 1.4px; padding: 10px 0 0 13px; }
  .subtitle-box { left: 71px; top: 193px; width: 243px; height: 30px; background: var(--navy); color: #fff;
    font-size: 18px; letter-spacing: 0.8px; padding: 0 0 0 13px; line-height: 24px; }

  .label { font-size: 13px; font-weight: 600; color: var(--ink); white-space: nowrap; }
  .line { height: 1px; background: var(--rule); }

  .heading { left: 71px; top: 608px; font-size: 15.5px; font-weight: 700; }

  .terms { left: 71px; top: 748px; width: 720px; font-size: 13px; line-height: 20px; font-weight: 600; color: var(--ink); white-space: nowrap; }

  .sig-label { font-size: 13px; font-weight: 600; }

  .footer-rule { left: 39px; top: 1089px; width: 770px; height: 2px; background: var(--navy); }
  .footer-col { top: 1100px; font-family: "Tinos", serif; font-size: 11.5px; line-height: 15px; color: #555a66; }
  .footer-col .row { display: flex; gap: 4px; align-items: center; }
  .footer-col .indent { padding-left: 13px; }
  .footer-col svg { width: 9px; height: 9px; fill: var(--ink); flex: none; }

  .base-band { left: 0; top: 1176px; width: 849px; height: 24px; }
</style>
</head>
<body>
<div class="sheet">

  <div class="abs brand">
    <div class="brand-mark"></div>
    <div class="brand-name">WohnKranich</div>
  </div>
  <div class="abs brand-tag">Vermietung und Hausverwaltung</div>

  <div class="abs title-box">BÜRGSCHAFTSURKUNDE</div>
  <div class="abs subtitle-box">für das Mietverhältnis</div>

  <div class="abs label" style="left:71px;top:326px;">zwischen dem Vermieter</div>
  <div class="abs line" style="left:248px;top:342px;width:529px;"></div>
  <div class="abs line" style="left:248px;top:370px;width:529px;"></div>

  <div class="abs label" style="left:71px;top:412px;">und dem Mieter</div>
  <div class="abs line" style="left:194px;top:427px;width:583px;"></div>
  <div class="abs line" style="left:194px;top:456px;width:583px;"></div>

  <div class="abs label" style="left:71px;top:526px;">für das Mietobjekt</div>
  <div class="abs line" style="left:208px;top:541px;width:569px;"></div>

  <div class="abs heading">Hiermit übernehme ich</div>

  <div class="abs label" style="left:71px;top:643px;">Vorname, Nachname</div>
  <div class="abs line" style="left:225px;top:658px;width:552px;"></div>
  <div class="abs label" style="left:71px;top:672px;">Anschrift:</div>
  <div class="abs line" style="left:152px;top:688px;width:625px;"></div>
  <div class="abs label" style="left:71px;top:700px;">Geboren am, in</div>
  <div class="abs line" style="left:189px;top:716px;width:588px;"></div>

  <div class="abs terms">
    die unbefristete, freiwillige und selbstschuldnerische Bürgschaft für den o. g. Mieter in dem o. g. Mietverhältnis.<br>
    Die Bürgschaft gilt für alle Mietzinsansprüche, Nachzahlung von Betriebskosten aus der jeweiligen Abrechnung<br>
    und einer evtl. stillschweigenden Verlängerung des Mietverhältnisses. Bei dieser Bürgschaft handelt es sich<br>
    um eine freiwillige, selbstschuldnerische Bürgschaft, die die Zahlung einer Mietkaution nicht ersetzt. Die<br>
    Bürgschaft gilt über die Kündigung, gemäß § 568 BGB, hinaus.<br>
    Ich verzichte ausdrücklich auf mir nach dem Gesetz zustehende Einreden, insbesondere auf die Einrede der<br>
    Anfechtung, der Aufrechnung und der Vorausklage und der Hinterlegung gemäß § § 770, 771 BGB.<br>
    Dieser Bürgschaftsurkunde lege ich eine Kopie meines Personalausweises bei.
  </div>

  <div class="abs line" style="left:71px;top:985px;width:263px;"></div>
  <div class="abs line" style="left:435px;top:985px;width:323px;"></div>
  <div class="abs sig-label" style="left:71px;top:988px;">Ort, Datum</div>
  <div class="abs sig-label" style="left:435px;top:988px;">Unterschrift des Bürgen</div>

  <div class="abs footer-rule"></div>

  <div class="abs footer-col" style="left:42px;">
    <div class="row"><svg viewBox="0 0 10 10"><path d="M5 0a3.5 3.5 0 0 0-3.5 3.5C1.5 6 5 10 5 10s3.5-4 3.5-6.5A3.5 3.5 0 0 0 5 0zm0 5a1.4 1.4 0 1 1 0-2.8A1.4 1.4 0 0 1 5 5z"/></svg>WohnKranich GmbH</div>
    <div class="indent">Kranichweg 16</div>
    <div class="indent">28195 Bremen</div>
  </div>

  <div class="abs footer-col" style="left:230px;">
    <div class="row"><svg viewBox="0 0 10 10"><path d="M2 0l2 2.5-1 1.2a6 6 0 0 0 3.3 3.3l1.2-1L10 8l-1.5 2C4 10 0 6 0 1.5z"/></svg>0421 55501234</div>
    <div class="row"><svg viewBox="0 0 10 10"><path d="M0 1.5h10v7H0zm1 1v.3l4 2.7 4-2.7v-.3zm0 1.5V7.5h8V4L5 6.6z"/></svg>info@wohnkranich.de</div>
    <div class="row"><svg viewBox="0 0 10 10"><path d="M5 0a5 5 0 1 0 0 10A5 5 0 0 0 5 0zm0 1a4 4 0 0 1 1.3.2C6.8 2.2 7 3.5 7 4.5H3c0-1 .2-2.3.7-3.3A4 4 0 0 1 5 1zM1 5.5h2c0 1.2.3 2.3.7 3.2A4 4 0 0 1 1 5.5zm6 0h2a4 4 0 0 1-2.7 3.2c.4-.9.7-2 .7-3.2zM1 4.5a4 4 0 0 1 2.7-3.2C3.3 2.2 3 3.3 3 4.5zm6 0c0-1.2-.3-2.3-.7-3.2A4 4 0 0 1 9 4.5zM4 5.5h2c0 1.2-.3 2.4-1 3.4-.7-1-1-2.2-1-3.4z"/></svg>www.wohnkranich.de</div>
  </div>

  <div class="abs footer-col" style="left:395px;">
    <div class="row"><svg viewBox="0 0 10 10"><path d="M5 0l5 2.5v1H0v-1zM1 4h1.5v4H1zm2.5 0H5v4H3.5zm2.5 0h1.5v4H6zm2 0h1v4H8zM0 8.5h10V10H0z"/></svg>Bankverbindung:</div>
    <div class="indent">Nordweser Sparkasse</div>
    <div class="indent">IBAN: DE00 1234 5678 9012 3456 78</div>
    <div class="indent">BIC.: NWSPDE21XXX</div>
  </div>

  <div class="abs footer-col" style="left:654px;">
    <div class="row"><svg viewBox="0 0 10 10"><circle cx="5" cy="2.8" r="2.5"/><path d="M0 10c0-3 2.2-4.5 5-4.5s5 1.5 5 4.5z"/></svg>Geschäftsführer:</div>
    <div class="indent">Jonas Berger &amp; Lea Marten</div>
    <div class="row"><svg viewBox="0 0 10 10"><path d="M1 0h8v10H1zm1.5 2v1h5V2zm0 2.2v1h5v-1zm0 2.2v1h3.5v-1z"/></svg>USt-ID-Nr.: DE000111222</div>
    <div class="indent">HRB 00000 HB</div>
  </div>

  <svg class="abs base-band" viewBox="0 0 849 24" aria-hidden="true">
    <rect width="849" height="24" fill="var(--navy)"/>
    <polygon points="645,24 650,0 656,0 651,24" fill="#ffffff"/>
  </svg>

</div>
</body>
</html>
```